Kanomiva business cards/stationary
Relocation Support Services
I need single sided standard sized Business Card [3.5" x 2"]
Designer's discretion
Professional
Ned Palmer
President
5-31-08 Nishimorino
Suginami-ku, Tokyo 168-0072
ned@kanomiva.com
www.kanomiva.com
Have not yet received logo files from designer. I will be using
Will upload Al format as soon as I receive from designer.
Kanomiva logo to be used

```html
<!DOCTYPE html>
<html lang="en">
<head>
<meta charset="utf-8">
<title>Kanomiva Business Card</title>
<link rel="stylesheet" href="https://fonts.googleapis.com/css2?family=PT+Sans:wght@400;700&display=swap">
<style>
  :root {
    --page-bg: #e9e6e2;
    --card-white: #ffffff;
    --brand-red: #c8102e;
    --deep-red: #9e0b22;
    --ink: #3a3a3a;
    --muted: #8a8a8a;
    --rule: #cfcfcf;
    --swoosh-dark: #2b2b2b;
    --swoosh-grey: #9a9a9a;
  }
  * { margin: 0; padding: 0; box-sizing: border-box; }
  html, body {
    width: 1200px; height: 780px; overflow: hidden;
    background: var(--page-bg);
    font-family: "PT Sans", Arial, sans-serif;
  }
  .business-card {
    position: absolute; left: 75px; top: 90px;
    width: 1050px; height: 600px;
    border-radius: 34px; overflow: hidden;
    background: var(--card-white);
    box-shadow: 0 10px 30px rgba(0,0,0,.18);
  }
  .card-waves { position: absolute; inset: 0; }
  .brand-block {
    position: absolute; left: 95px; top: 175px; width: 360px;
    display: flex; flex-direction: column; align-items: flex-start;
  }
  .brand-row { display: flex; align-items: center; gap: 14px; }
  .brand-dot {
    width: 34px; height: 34px; border-radius: 50%;
    background: var(--brand-red);
  }
  .brand-name {
    font-size: 58px; font-weight: 700; color: var(--brand-red);
    line-height: 1; letter-spacing: -0.5px;
  }
  .brand-tagline {
    margin-top: 8px; margin-left: 150px;
    font-size: 21px; font-weight: 700; color: var(--brand-red);
  }
  .divider {
    position: absolute; left: 500px; top: 40px;
    width: 2px; height: 300px; background: var(--rule);
  }
  .contact-block { position: absolute; left: 540px; top: 48px; color: var(--ink); }
  .person-name { font-size: 40px; font-weight: 700; color: var(--brand-red); line-height: 1.1; }
  .person-title { font-size: 26px; color: var(--muted); margin-top: 2px; }
  .address { margin-top: 78px; font-size: 26px; line-height: 1.3; }
  .contact-list { list-style: none; margin-top: 10px; font-size: 26px; }
  .contact-list li { display: flex; align-items: center; gap: 10px; height: 40px; }
  .contact-icon { width: 24px; height: 24px; flex: none; }
</style>
</head>
<body>
  <div class="business-card">
    <svg class="card-waves" width="1050" height="600" viewBox="0 0 1050 600" aria-hidden="true">
      <path d="M0,488 C300,560 700,540 1050,440 L1050,600 L0,600 Z" fill="var(--brand-red)"/>
      <path d="M0,530 C320,590 700,575 1050,500 L1050,600 L0,600 Z" fill="var(--deep-red)" opacity=".35"/>
      <path d="M0,462 C300,520 700,505 1050,420 L1050,432 C700,522 300,536 0,478 Z" fill="var(--swoosh-dark)"/>
      <path d="M0,478 C300,536 700,522 1050,432 L1050,442 C700,532 300,548 0,488 Z" fill="var(--swoosh-grey)"/>
    </svg>

    <div class="brand-block">
      <div class="brand-row">
        <span class="brand-dot"></span>
        <span class="brand-name">Kanomiva</span>
      </div>
      <div class="brand-tagline">Relocation Services</div>
    </div>

    <div class="divider"></div>

    <div class="contact-block">
      <div class="person-name">Ned Palmer</div>
      <div class="person-title">President</div>
      <div class="address">5-31-08 Nishimorino<br>Suginami-ku, Tokyo 168-0072</div>
      <ul class="contact-list">
        <li>
          <svg class="contact-icon" viewBox="0 0 24 24" aria-label="Phone"><path d="M6.6 10.8a15 15 0 0 0 6.6 6.6l2.2-2.2c.3-.3.7-.4 1-.2 1.1.4 2.3.6 3.6.6.6 0 1 .4 1 1V20c0 .6-.4 1-1 1A17 17 0 0 1 3 4c0-.6.4-1 1-1h3.5c.6 0 1 .4 1 1 0 1.3.2 2.5.6 3.6.1.3 0 .7-.2 1z" fill="var(--brand-red)"/></svg>
          <span>+81 (0)80-4512-3986</span>
        </li>
        <li>
          <svg class="contact-icon" viewBox="0 0 24 24" aria-label="Email"><circle cx="12" cy="12" r="11" fill="var(--brand-red)"/><text x="12" y="17" text-anchor="middle" font-size="15" font-weight="700" fill="#fff" font-family="PT Sans, sans-serif">@</text></svg>
          <span>ned@kanomiva.com</span>
        </li>
        <li>
          <svg class="contact-icon" viewBox="0 0 24 24" aria-label="Website"><circle cx="12" cy="12" r="10" fill="none" stroke="var(--brand-red)" stroke-width="2"/><ellipse cx="12" cy="12" rx="4" ry="10" fill="none" stroke="var(--brand-red)" stroke-width="1.5"/><path d="M2 12h20" stroke="var(--brand-red)" stroke-width="1.5"/></svg>
          <span>www.kanomiva.com</span>
        </li>
      </ul>
    </div>
  </div>
</body>
</html>
```